" Window Blinds and Shutters Business Card Design"

We require a business card design for a new windows blinds and shutters company based in Sydney.
The business name is 'Harbourlight Blinds and Shutters'.
We supply and install homes and businesses with internal and external window furnishings and finishes. This includes varieties of window blinds and window shutters.

Benefits of Harbourlight Blinds and Shutters :
Added security and privacy,
The ability to control the amount of sunlight,
Regulate internal temperature.

Blinds varieties:
Roller Blinds, Double Roller Blinds, Roman Blinds, Vertical Blinds, Aluminium venetians, Timber venetians and PVC Venetians.

Shutters varieties:
Plantation Shutters, Aluminium Louvre Shutters, Roller Shutters and Security Shutters .

Hi Designers,

Please have a look at my Business card design brief. I need your help to start my new business.

Thanks,

Daniel.

Reason: not 100% happy with the options available, close to 90% happy, need a little more refinement. Thank You & Good Luck

Target Market(s)

Home owners, business owners, shift workers , and new home builders.

Industry/Entity Type

Security

Contact Information for Business Card

Harbourlight Blinds and Shutters,

Daniel Brostow mobile: 0417586204,
Corey Wendt mobile: 0419248653,

email: daniel.brostow@mailvista.net
web: harbourlightblindsandshutters.com.au

Colors
ffffff
9d9d9d
f78f20

Requirements
Must have
• ON FRONT OF CARD
I have attached a picture of logo and need a designer to design a font logo for Harbourlight Blinds and Shutters similar, or open to suggestions.

FRONT OF CARD
Company message/:
"Protecting windows with style"

BACK OF CARD
'For a FREE measure & quote call Daniel - 0417586204"
Nice to have
• Elegant yet professional.

Soft colours appealing to both male & female clients.

Should not have

• Unprofessional fonts

```html
<!DOCTYPE html>
<html lang="en">
<head>
<meta charset="utf-8">
<title>Harbourlight Blinds and Shutters – Business Card</title>
<link rel="stylesheet" href="https://fonts.googleapis.com/css2?family=Tinos:wght@400;700&display=swap">
<style>
  :root {
    --page: #ffffff;
    --sky-blue: #3d7ab8;
    --deep-blue: #3d5c9a;
    --ink: #000000;
    --text-light: #ffffff;
  }
  html, body {
    margin: 0;
    padding: 0;
    width: 1200px;
    height: 741px;
    overflow: hidden;
    background: var(--page);
  }
  .card {
    display: block;
    width: 1200px;
    height: 741px;
  }
  .band-top { fill: var(--sky-blue); }
  .band-middle { fill: var(--deep-blue); }
  .band-base, .contact-tab { fill: var(--ink); }
  .card text {
    font-family: "Tinos", "Times New Roman", serif;
    fill: var(--text-light);
  }
  .brand-name { font-size: 122px; font-weight: 400; }
  .tagline { font-size: 72px; font-weight: 400; }
  .contact-line { font-size: 47px; font-weight: 700; }
  .contact-line .number-light { font-weight: 400; }
</style>
</head>
<body>
<svg class="card" viewBox="0 0 1200 741" xmlns="http://www.w3.org/2000/svg">
  <rect class="band-top" x="43" y="45" width="1114" height="334"/>
  <rect class="band-middle" x="43" y="378" width="1114" height="102"/>
  <rect class="band-base" x="43" y="479" width="1114" height="218"/>
  <path class="contact-tab" d="M178 378 H864 L898 400 V480 H157 V400 Q157 378 178 378 Z"/>

  <text class="brand-name" x="108" y="222" textLength="1016" lengthAdjust="spacingAndGlyphs">Harbourlight Blinds and Shutters</text>
  <text class="tagline" x="246" y="319" textLength="764" lengthAdjust="spacingAndGlyphs">Protecting windows with style</text>

  <text class="contact-line" x="180" y="449" textLength="687" lengthAdjust="spacingAndGlyphs">Daniel Brostow mobile: <tspan class="number-light">0417586204</tspan></text>
  <text class="contact-line" x="180" y="509" textLength="600" lengthAdjust="spacingAndGlyphs">Corey Wendt mobile: 0419248653</text>
  <text class="contact-line" x="180" y="569" textLength="955" lengthAdjust="spacingAndGlyphs">Business Partners email: daniel.brostow@mailvista.net</text>
  <text class="contact-line" x="180" y="631" textLength="768" lengthAdjust="spacingAndGlyphs">Web: harbourlightblindsandshutters.com.au</text>
</svg>
</body>
</html>
```